Electrical contracting business specialising in smoke detector installation needs flyer design

i need a flyer design made up highlighting the fact that the Qld legislation is changing on smoke detectors in homes for everyones safety. I am an electrical contractor ( Tallow Bend Electrical) specialising in smoke detector installation to comply with the new Qld legislation. Some of the wording that can be used-
When you sleep, your sense of smell also sleeps. If a fire starts, toxic fumes canovercome you. Photoelectric smoke alarms see smoke and will alert you early, so you can escape. With interconnected alarms, you will be alerted no matter where you are, or where the fire starts.
New legislation specifies the type, positioning and interconnectedness of alarms, which are critical factors for an early warning and a quick escape.
To give your family the best chance of surviving a house fire, update your smoke alarms to match the new legislation as soon as you can. Call ME on 0471385269

Target Market(s)

Body Corporates , people selling and renting their properties

Industry/Entity Type

Electrician

Colors

Designer to choose colors to be used in the design.

Requirements
Must have
• Safety aspect.

```html
<!DOCTYPE html>
<html lang="en">
<head>
<meta charset="utf-8">
<title>Smoke Alarm Legislation Flyer – Tallow Bend Electrical</title>
<link rel="stylesheet" href="https://fonts.googleapis.com/css2?family=Josefin+Sans:wght@600;700&family=Questrial&family=Ubuntu:wght@500&display=swap">
<style>
  :root {
    --page-bg: #e6e3df;
    --flyer-bg: #0b0b0c;
    --flyer-bg-edge: #151517;
    --ink-light: #ffffff;
    --ink-soft: #e4e4e4;
    --ink-dark: #111111;
    --hero-deep: #0a1322;
    --hero-mid: #2c5c86;
    --rule: #9a9a9a;
  }
  * { margin: 0; padding: 0; box-sizing: border-box; }
  html, body { width: 1200px; height: 1200px; overflow: hidden; }
  body {
    background: var(--page-bg);
    font-family: "Questrial", "Century Gothic", sans-serif;
    color: var(--ink-light);
    position: relative;
  }
  .flyer {
    position: absolute;
    left: 185px; top: 30px;
    width: 830px; height: 1140px;
    background: radial-gradient(ellipse at 50% 45%, var(--flyer-bg-edge), var(--flyer-bg) 75%);
  }
  .hero {
    position: absolute;
    left: 51px; top: 49px; width: 727px; height: 308px;
    border: 5px solid var(--ink-light);
    background:
      radial-gradient(ellipse at 55% 75%, rgba(127,200,239,0.55), transparent 60%),
      linear-gradient(180deg, var(--hero-deep) 0%, #15263d 40%, var(--hero-mid) 80%, #9fb6c9 100%);
    overflow: hidden;
  }
  .hero-kicker {
    position: absolute; left: 10px; top: 12px;
    font-family: "Ubuntu", sans-serif; font-weight: 500;
    font-size: 22px; color: var(--ink-soft);
  }
  .hero-title {
    position: absolute; left: 9px; top: 42px;
    font-family: "Ubuntu", sans-serif; font-weight: 500;
    font-size: 44px; color: var(--ink-light);
  }
  .lead-head {
    position: absolute; left: 55px; top: 382px; width: 723px;
    font-family: "Josefin Sans", sans-serif; font-weight: 700;
    font-size: 24px; letter-spacing: 0; white-space: nowrap;
  }
  .lead-body {
    position: absolute; left: 55px; top: 416px; width: 725px;
    font-size: 16.3px; line-height: 20.4px; color: var(--ink-soft);
  }
  .law-banner {
    position: absolute; left: 51px; top: 499px; width: 727px; height: 48px;
    background: var(--ink-light); color: var(--ink-dark);
    font-family: "Josefin Sans", sans-serif; font-weight: 700;
    font-size: 38px; line-height: 54px; text-align: center; letter-spacing: 0;
    white-space: nowrap;
  }
  .law-source {
    position: absolute; left: 51px; top: 549px; width: 727px;
    display: flex; align-items: center; gap: 8px;
    font-size: 19px; color: var(--ink-soft);
  }
  .law-source .rule { flex: 1; height: 1px; background: var(--rule); }
  .law-body {
    position: absolute; left: 58px; top: 577px; width: 720px;
    font-size: 16.3px; line-height: 20.4px; color: var(--ink-soft);
  }
  .cta {
    position: absolute; left: 51px; top: 637px; width: 727px; height: 117px;
    border: 3px solid var(--ink-light); text-align: center;
  }
  .cta-text {
    margin: 10px 14px 0; font-size: 16.3px; line-height: 20.4px; color: var(--ink-soft);
  }
  .cta-phone {
    font-family: "Josefin Sans", sans-serif; font-weight: 700;
    font-size: 41px; line-height: 50px; margin-top: 6px; letter-spacing: 0.3px;
    white-space: nowrap;
  }
  .glossary {
    position: absolute; left: 51px; top: 786px; width: 727px; text-align: center;
  }
  .glossary h2 {
    font-family: "Josefin Sans", sans-serif; font-weight: 700;
    font-size: 29px; letter-spacing: 0.3px; margin-bottom: 10px;
  }
  .glossary p {
    font-size: 17px; line-height: 20.1px; color: var(--ink-soft);
  }
  .contact-bar {
    position: absolute; left: 51px; top: 1034px; width: 727px; height: 49px;
    background: var(--ink-light); color: var(--ink-dark);
    text-align: center; font-size: 16px; line-height: 18px; padding-top: 6px;
  }
  .contact-bar strong { font-family: "Josefin Sans", sans-serif; font-weight: 700; }
</style>
</head>
<body>
  <main class="flyer">
    <section class="hero" role="img" aria-label="Illustration of a house floor plan with interconnected ceiling smoke alarms casting blue detection cones as a person runs from a fire in a bedroom">
      <p class="hero-kicker">Are you up to speed with</p>
      <h1 class="hero-title">smoke alarms?</h1>
    </section>

    <h2 class="lead-head">WHEN YOU SLEEP, YOUR SENSE OF SMELL ALSO SLEEPS.</h2>
    <p class="lead-body">If a fire starts, toxic fumes canovercome you. Photoelectric smoke alarms see smoke and will alert you early, so you can escape. With interconnected alarms, you will be alerted no matter where you are, or where the fire starts.</p>

    <div class="law-banner">NEW SMOKE ALARM LEGISLATION</div>
    <div class="law-source"><span class="rule"></span><span>Regional Fire Safety Office</span></div>
    <p class="law-body">New legislation specifies the type, positioning and interconnectedness of alarms, which are critical factors for an early warning and a quick escape.</p>

    <section class="cta">
      <p class="cta-text">To give your family the best chance of surviving a house fire, update your smoke alarms to match the new legislation as soon as you can.</p>
      <p class="cta-phone">CALL ME ON 0471385269</p>
    </section>

    <section class="glossary">
      <h2>GLOSSARY OF TERMS*</h2>
      <p>Dwellings - houses, townhouses (Class 1A) and units (Class 2).<br>
      Photoelectric - the method the device uses to detect smoke.<br>
      Hardwired - connected to the domestic dwelling’s electricity supply.<br>
      Interconnected - if one smoke alarm sounds all the other smoke<br>
      alarms will also sound. Interconnection can be wired or wireless.<br>
      Substantial - work carried out under a building development approval<br>
      or the total building works equals 50% of the dwelling over 3 years.<br>
      Storey - a space within a building which is situated between one floor<br>
      level and the floor level or roof above.</p>
    </section>

    <footer class="contact-bar">
      If you have a specific question or require further clarification, please<br>
      <strong>email alarmhelp@firesafetyoffice.org.</strong>
    </footer>
  </main>
</body>
</html>
```